Need a business card design. I am a Self Empowerment Life Coach.

A Life Coach is - a professional relationship designed to enhance an individual's ability to focus, make effective changes, develop oneself, achieve desired goals and maximize success in life. Coaching is about getting the very best out of someone and enabling them to make decisions that will improve their life. It is a unique way to help people look at where they are now and where they would like to be, and helps bridge the gap.

Tidal Grove Coaching is motivational, inspiring, positive, exciting and action driven. By raising awareness and encouraging others to take responsibility for their life, coaching can help people rise to their challenge and go further than you ever thought possible.

Industry/Entity Type

Business

Font styles to use
Other font styles liked:
• Bookman Old Style

Requirements
Must have
• Marlena Voskuil, ELI-MP
• Self Empowerment Coach
• 358.617.2083
• mv@thebrightpathguide.net
• The attached logo
Nice to have
• I would like to see some designs portrait and some landscape

```html
<!DOCTYPE html>
<html lang="en">
<head>
<meta charset="utf-8">
<title>Tidal Grove Coaching – Business Card</title>
<link rel="stylesheet" href="https://fonts.googleapis.com/css2?family=Comic+Neue:wght@400;700&family=Montserrat:wght@400;500&display=swap">
<style>
  :root {
    --page-bg: #f1f2f4;
    --card-bg: #ffffff;
    --card-edge: #e4e5e8;
    --ink-blue: #2a5db0;
    --brand-navy: #1d4f91;
    --brand-sky: #2d8fd5;
    --rule-grey: #6b6f78;
    --icon-grey: #4a4d55;
    --deco-yellow: #fbf3d6;
    --deco-grey: #ebebee;
  }
  * { margin: 0; padding: 0; box-sizing: border-box; }
  html, body {
    width: 1000px; height: 1200px; overflow: hidden;
    background: var(--page-bg);
  }
  .stage {
    position: relative; width: 1000px; height: 1200px;
    display: flex; align-items: center; justify-content: center;
  }
  .business-card {
    position: relative; width: 840px; height: 480px;
    background: var(--card-bg);
    border: 1px solid var(--card-edge);
    box-shadow: 0 6px 18px rgba(0,0,0,0.08);
    overflow: hidden;
  }
  .background-decoration {
    position: absolute; left: 40px; top: 150px; width: 520px; height: 360px;
    border-radius: 50% 50% 40% 40%;
    background: radial-gradient(ellipse at 35% 45%, var(--deco-yellow) 0%, var(--deco-yellow) 40%, var(--deco-grey) 75%, rgba(255,255,255,0) 100%);
    opacity: 0.8;
  }
  .brand-block {
    position: absolute; right: 40px; top: 56px; width: 280px;
    text-align: center;
  }
  .brand-mark {
    display: block; width: 22px; height: 22px; border-radius: 50%;
    background: var(--brand-sky); margin: 0 auto 14px;
  }
  .brand-name {
    font-family: "Comic Neue", sans-serif; font-weight: 700;
    font-size: 40px; line-height: 1.1; color: var(--brand-navy);
  }
  .tagline-rule {
    height: 2px; background: var(--rule-grey); margin: 22px 0 8px;
  }
  .tagline-lead {
    font-family: "Montserrat", sans-serif; font-weight: 500;
    font-size: 14px; letter-spacing: 1px; color: var(--brand-navy);
  }
  .tagline-punch {
    font-family: "Montserrat", sans-serif; font-weight: 400;
    font-size: 50px; letter-spacing: 6px; color: var(--brand-navy);
    line-height: 1.1;
  }
  .contact-block {
    position: absolute; left: 48px; bottom: 40px;
    font-family: "Comic Neue", sans-serif; font-weight: 400;
    font-size: 27px; line-height: 1.22; color: var(--ink-blue);
  }
  .contact-line { display: flex; align-items: center; }
  .contact-line.indented { padding-left: 36px; }
  .contact-icon { width: 26px; height: 22px; margin-right: 10px; flex: none; }
</style>
</head>
<body>
<main class="stage">
  <section class="business-card">
    <div class="background-decoration" role="img" aria-label="Faint cheerful waving character illustration as background decoration"></div>

    <div class="brand-block">
      <span class="brand-mark"></span>
      <div class="brand-name">Tidal Grove Coaching</div>
      <div class="tagline-rule"></div>
      <div class="tagline-lead">MOVE FROM MAYBE TO</div>
      <div class="tagline-punch">YES!</div>
    </div>

    <div class="contact-block">
      <p class="contact-line indented">Marlena Voskuil, ELI-MP</p>
      <p class="contact-line indented">Self Empowerment Coach</p>
      <p class="contact-line">
        <svg class="contact-icon" viewBox="0 0 26 22" aria-hidden="true">
          <path d="M2 8 Q13 0 24 8 L21 11 L17 8 L9 8 L5 11 Z" fill="var(--icon-grey)"/>
          <rect x="6" y="11" width="14" height="9" rx="2" fill="var(--icon-grey)"/>
          <circle cx="13" cy="15.5" r="2.5" fill="#fff"/>
        </svg>358.617.2083</p>
      <p class="contact-line">
        <svg class="contact-icon" viewBox="0 0 26 22" aria-hidden="true">
          <rect x="2" y="4" width="22" height="15" fill="var(--icon-grey)"/>
          <path d="M2 4 L13 13 L24 4" fill="none" stroke="#fff" stroke-width="1.6"/>
        </svg>mv@thebrightpathguide.net</p>
    </div>
  </section>
</main>
</body>
</html>
```